B2B Software Company Needs 300x250 banner ad

I need a 300x250 static gif banner ad for a web site/online newsletter that we advertise on. We're a B2B software company, and the audience for this banner ad is medical device development team leads and managers. We would like to see designs that use blue (mainly), accent colors of orange, bright green, and purple are OK, too. This is a text heavy add but that can't be changed. I'm attaching our corporate logo, the copy file (Harbor Ledger.doc), latest version of our style guide, and an example of a previous ad we've done (which we don't necessarily need to/want to recreate). We want something that is pleasing to look at, easy to read, and gets someone to click through to the landing page.

Industry/Entity Type

Software

Requirements
Should not have
• Please do not re-lay out the 2013 outlook of Clinical Hardware Engineering banner. That was simply uploaded as an example. The docx Word document/copy should be used for a new banner ad.

```html
<!DOCTYPE html>
<html lang="en">
<head>
<meta charset="UTF-8">
<title>White Paper Banner</title>
<link href="https://fonts.googleapis.com/css2?family=Open+Sans:wght@400;600;700;800&display=swap" rel="stylesheet">
<style>
  :root {
    --blue-light: #2485d6;
    --blue-dark: #1363b3;
    --white: #ffffff;
    --green: #8ed43a;
    --dash: #9cc6ee;
    --ink: #3a3a3a;
    --logo-blue: #1f6fc0;
    --orange-top: #f0782e;
    --orange-bottom: #d4531a;
  }
  * { margin: 0; padding: 0; box-sizing: border-box; }
  html, body { width: 1200px; height: 999px; overflow: hidden; background: var(--white); }
  .banner {
    position: relative;
    width: 1200px;
    height: 999px;
    font-family: "Open Sans", Arial, sans-serif;
  }
  .hero {
    position: absolute;
    inset: 0 0 auto 0;
    height: 726px;
    background: radial-gradient(ellipse at 50% 40%, var(--blue-light) 0%, var(--blue-dark) 100%);
    text-align: center;
    color: var(--white);
  }
  .eyebrow {
    position: absolute;
    top: 96px;
    width: 100%;
    font-size: 61px;
    font-weight: 800;
    letter-spacing: 0.5px;
  }
  .headline {
    position: absolute;
    top: 188px;
    width: 100%;
    font-size: 55px;
    line-height: 74px;
    font-weight: 600;
    color: var(--green);
  }
  .divider {
    position: absolute;
    top: 390px;
    left: 99px;
    width: 1002px;
    border-top: 3px dashed var(--dash);
  }
  .summary {
    position: absolute;
    top: 423px;
    width: 100%;
    font-size: 46px;
    line-height: 71px;
    font-weight: 400;
  }
  .summary strong { font-weight: 700; }
  .brand {
    position: absolute;
    left: 78px;
    top: 810px;
    display: flex;
    align-items: center;
    gap: 22px;
  }
  .brand-mark {
    width: 66px;
    height: 66px;
    background: var(--logo-blue);
  }
  .brand-name {
    font-size: 58px;
    font-weight: 600;
    color: var(--ink);
    line-height: 1;
  }
  .cta {
    position: absolute;
    left: 675px;
    top: 792px;
    width: 483px;
    height: 123px;
    border-radius: 14px;
    background: linear-gradient(var(--orange-top), var(--orange-bottom));
    color: var(--white);
    font-size: 50px;
    font-weight: 700;
    display: flex;
    align-items: center;
    justify-content: center;
    gap: 24px;
    text-decoration: none;
  }
  .cta svg { width: 26px; height: 40px; }
</style>
</head>
<body>
  <div class="banner">
    <section class="hero">
      <h1 class="eyebrow">EXCLUSIVE WHITE PAPER:</h1>
      <h2 class="headline">EXPOSING RISK IN PRODUCT<br>DEVELOPMENT LIFECYCLES</h2>
      <div class="divider"></div>
      <p class="summary">Reduce time spent managing risk<br>and support regulatory approvals with<br><strong>traceability-based</strong> risk management</p>
    </section>
    <div class="brand">
      <span class="brand-mark"></span>
      <span class="brand-name">Tidewell Software</span>
    </div>
    <a class="cta" href="#">READ NOW
      <svg viewBox="0 0 26 40" aria-hidden="true"><polyline points="5,5 20,20 5,35" fill="none" stroke="#ffffff" stroke-width="7"/></svg>
    </a>
  </div>
</body>
</html>
```